Classy, Elegant, Simple Business Card Design

Looking to have a classy, simple, and elegant design. Want a top notch designed business card. I really like the look of the new brivo credit card. I also like the design I attached. I am trying to reach 21-29 year old females for booking us for there wedding or event. We offer Disc Jockey Service, Photo Booth Rentals, and Uplighting .

Target Market(s)

21-28 year old females

Contact Information for Business Card

Has to have logo, website, email, and phone number

Font styles to use
Other font styles liked:
• open to font choice, modern, clean
Designer to choose
33a6d7
0791cd
0555a3
ffffff

Requirements
Must have
• Has to have logo, website, email, and phone number
Nice to have
• I really like the design of the new brivo credit card. I also included my logo and some designs I like
Should not have
• clutter or too much info

```html
<!DOCTYPE html>
<html lang="en">
<head>
<meta charset="utf-8">
<title>Tidepool Events – Business Card</title>
<link href="https://fonts.googleapis.com/css2?family=Jost:wght@400&family=Roboto:wght@400;500&display=swap" rel="stylesheet">
<style>
  :root{
    --stage:#808080;
    --sky-top:#24a9e1;
    --sky-bottom:#0f6fb6;
    --navy:#0e2f5c;
    --brand-blue:#0a64b8;
    --ink:#1b1b1b;
    --paper:#ffffff;
  }
  html,body{margin:0;padding:0;overflow:hidden}
  body{width:1200px;height:1020px;background:var(--stage);position:relative;font-family:"Roboto",Arial,sans-serif}
  .card{position:absolute;left:271px;width:657px;height:376px;overflow:hidden}
  .card-front{top:87px;background:linear-gradient(180deg,var(--sky-top),var(--sky-bottom))}
  .card-back{top:514px;background:var(--paper)}

  .brand{display:flex;align-items:center;gap:10px;font-family:"Jost",Arial,sans-serif;font-weight:400;letter-spacing:2px;text-transform:uppercase;line-height:1}
  .brand-dot{border-radius:50%;flex:none}
  .card-front .brand{position:absolute;left:0;right:0;top:170px;justify-content:center;color:var(--navy);font-size:36px}
  .card-front .brand-dot{width:22px;height:22px;background:var(--navy)}
  .card-back .brand{position:absolute;left:25px;top:124px;color:var(--brand-blue);font-size:26px}
  .card-back .brand-dot{width:17px;height:17px;background:var(--brand-blue)}

  .holder{position:absolute;right:22px;top:60px;text-align:right}
  .holder-name{font-size:26px;color:var(--navy);letter-spacing:.5px;line-height:1}
  .holder-name strong{color:var(--brand-blue);font-weight:500}
  .holder-role{font-size:17px;color:var(--ink);margin-top:10px;line-height:1.2}

  .address{position:absolute;left:25px;top:192px;font-size:18px;line-height:24px;color:var(--ink);letter-spacing:.4px}
  .contacts{position:absolute;left:25px;top:254px;margin:0;padding:0;list-style:none}
  .contacts li{display:flex;align-items:center;height:26px;font-size:18px;line-height:26px;color:var(--ink);letter-spacing:.4px}
  .contacts svg{width:16px;height:16px;margin-right:9px;fill:var(--brand-blue);flex:none}
  .contacts .accent{color:var(--brand-blue)}
</style>
</head>
<body>
  <section class="card card-front">
    <div class="brand"><span class="brand-dot"></span>Tidepool Events</div>
  </section>

  <section class="card card-back">
    <div class="brand"><span class="brand-dot"></span>Tidepool Events</div>

    <div class="holder">
      <div class="holder-name">DANA <strong>ROWELL</strong></div>
      <div class="holder-role">Founder &amp; CEO</div>
    </div>

    <div class="address">214 Harbor Lane<br>Seacliff, CA 90000</div>

    <ul class="contacts">
      <li><svg viewBox="0 0 16 16"><path d="M4.5 0h7A1.5 1.5 0 0 1 13 1.5v13a1.5 1.5 0 0 1-1.5 1.5h-7A1.5 1.5 0 0 1 3 14.5v-13A1.5 1.5 0 0 1 4.5 0zM4.6 1.6v12.8h6.8V1.6z"/></svg>555-014-2286</li>
      <li><svg viewBox="0 0 16 16"><path d="M3.6 1l2.4 2.9-1.4 1.8c.9 2.1 2.6 3.8 4.7 4.7l1.8-1.4L14 11.4 12.3 14C6.6 13.7 2.3 9.4 2 3.7z"/></svg>555-017-9031</li>
      <li><svg viewBox="0 0 16 16"><path d="M1 3h14v10H1zM2.4 4.4v.3L8 8.6l5.6-3.9v-.3zM2.4 6.4v5.2h11.2V6.4L8 10.3z"/></svg>hello@tidepoolevents.com</li>
      <li><svg viewBox="0 0 16 16"><circle cx="8" cy="8" r="7"/><path d="M5 4.5c1.3.3 1.8 1.4 1 2.4-.6.7.2 1.8 1.2 1.7 1 0 1 1.5.3 2.4M10 3.2c-.6 1-.2 2.1 1 2.2M12.8 9.5c-1.2-.4-2 .4-1.8 1.7" fill="none" stroke="#fff" stroke-width="1.1"/></svg>www.<span class="accent">tidepoolevents</span>.com</li>
    </ul>
  </section>
</body>
</html>
```